Coach/consultant in conflict and challenge needs an enticing flyer

I need a double sided DL flyer design that will describe my work in helping people meet conflict and emotional challenge so they can learn and grow from these difficulties. I want to give a flavour of my style through fresh colours, repeated images used differently (the spiral), and a sense of positivity around conflict and difficulty. I want to attract people who are keen to do things differently and want to engage with creative processes rather than getting stuck in familiar patterns. My work is creative and often includes use of story, images and fables, so I want to convey that as well. I also place the work in a spiritual context, but grounded in practicality so I don't want it to seem New Age or flakey. I want something that seems innovative, professional and intriguing. I've included a sample of something I mocked up in word and also a copy of a flyer for Marla Quennet's Ember Gathering that inspired me to get a DL flyer. I want the design to communicate trust and transformation and engaging with fresh ways of doing things by moving past old habits

Target Market(s)

Mid 30s plus women and men who want to change their approach to conflict and emotional difficulties and are willing to take the creative and challenging journey to do that

Industry/Entity Type

Learn

Colors
acd136
00a990

Requirements
Must have
• a shift in the use of the spiral image,
• use of image of me (Norah)
• bright fresh colours olours that represent growth and transformation--I've suggested lime green as it suggests a sense of growth
• easy to read text
Nice to have
• Interesting non-traditional fonts perhaps text in a contemporary sans serif and another brush script font (like the Ember Gathering example)
• bleed to the edge and run off the page images or text
Should not have
• anything that represents too much tradition or stuckness

```html
<!DOCTYPE html>
<html lang="en">
<head>
<meta charset="utf-8">
<title>Norah Castell – DL Flyer</title>
<link rel="stylesheet" href="https://fonts.googleapis.com/css2?family=Ubuntu:wght@300;400;500&display=swap">
<style>
  :root {
    --teal: #00a990;
    --teal-dark: #0a9a84;
    --lime: #acd136;
    --green-soft: #5cc48a;
    --green-deep: #2fb37a;
    --ink: #222222;
    --white: #ffffff;
    --footer: #2a2a2a;
    --page: #ecece8;
  }
  * { margin: 0; padding: 0; box-sizing: border-box; }
  html, body { width: 960px; height: 1200px; overflow: hidden; }
  body { background: var(--page); font-family: "Ubuntu", Arial, sans-serif; position: relative; }

  .flyer { position: absolute; left: 40px; width: 880px; height: 440px; overflow: hidden; box-shadow: 0 8px 18px rgba(0,0,0,.25); }
  .flyer-front { top: 120px; background: var(--white); }
  .flyer-back { top: 640px; }
  .flyer svg.shapes { position: absolute; inset: 0; }

  .front-name { position: absolute; left: 34px; top: 26px; font-size: 54px; font-weight: 500; color: var(--teal); letter-spacing: .5px; }
  .front-values { position: absolute; left: 35px; top: 88px; font-size: 23px; font-weight: 400; color: var(--ink); }
  .front-values span + span { border-left: 1.5px solid var(--ink); padding-left: 6px; margin-left: 6px; }
  .front-intro { position: absolute; left: 35px; top: 136px; width: 440px; font-size: 15.5px; line-height: 19px; color: var(--ink); }
  .front-about { position: absolute; left: 35px; top: 358px; width: 500px; font-size: 18.5px; line-height: 22.5px; color: var(--white); font-weight: 400; }

  .back-name { position: absolute; left: 20px; top: 22px; font-size: 62px; font-weight: 400; color: var(--white); }
  .back-credentials { position: absolute; left: 20px; top: 92px; font-size: 19px; color: var(--white); }
  .back-copy { position: absolute; left: 20px; top: 128px; width: 570px; font-size: 15px; line-height: 18px; color: var(--white); }
  .back-copy p + p { margin-top: 10px; }
  .back-services { position: absolute; left: 20px; top: 286px; width: 560px; border-top: 1px solid rgba(255,255,255,.6); padding-top: 14px; display: flex; gap: 36px; list-style: none; font-size: 15.5px; color: var(--white); }
  .back-services li { display: flex; align-items: center; gap: 10px; }
  .back-services svg { width: 14px; height: 14px; }

  .back-footer { position: absolute; left: 0; bottom: 0; width: 880px; height: 88px; background: var(--footer); color: var(--white); font-size: 15.5px; }
  .contact { position: absolute; display: flex; align-items: center; gap: 14px; }
  .contact svg { width: 16px; height: 16px; }
  .contact-mobile { left: 32px; top: 23px; }
  .contact-phone { left: 32px; top: 46px; }
  .contact-email { left: 342px; top: 22px; }
  .contact-web { left: 342px; top: 45px; }
  .business-number { position: absolute; right: 32px; top: 34px; }
</style>
</head>
<body>

<section class="flyer flyer-front">
  <svg class="shapes" width="880" height="440" viewBox="0 0 880 440">
    <defs>
      <linearGradient id="foliage" x1="0" y1="0" x2="1" y2="0">
        <stop offset="0" stop-color="#e8f4df" stop-opacity="0"/>
        <stop offset=".45" stop-color="#b9df8f" stop-opacity=".7"/>
        <stop offset="1" stop-color="#6fc24a"/>
      </linearGradient>
      <radialGradient id="portrait" cx=".5" cy=".45" r=".6">
        <stop offset="0" stop-color="#d9b8a0"/>
        <stop offset=".55" stop-color="#b98f70"/>
        <stop offset="1" stop-color="#e8612a"/>
      </radialGradient>
    </defs>
    <rect class="foliage-photo" x="300" y="0" width="580" height="340" fill="url(#foliage)" role="img" aria-label="Photograph of fresh green leaves on a branch"/>
    <path d="M0 290 C 120 220, 260 250, 380 290 S 560 345, 620 350 L 620 440 L 0 440 Z" fill="var(--lime)"/>
    <path d="M0 312 C 120 248, 260 270, 380 305 S 560 355, 620 360 L 620 440 L 0 440 Z" fill="var(--white)"/>
    <path d="M0 320 C 120 262, 260 282, 380 315 S 560 362, 620 366 L 620 440 L 0 440 Z" fill="var(--teal)"/>
    <circle cx="725" cy="270" r="188" fill="var(--lime)"/>
    <circle cx="725" cy="270" r="178" fill="var(--white)"/>
    <circle cx="725" cy="278" r="165" fill="url(#portrait)" role="img" aria-label="Portrait photograph of Norah Castell in an orange top"/>
  </svg>
  <h1 class="front-name">Norah Castell</h1>
  <p class="front-values"><span>courage</span><span>listening</span><span>creativity</span></p>
  <p class="front-intro">Challenge, change and conflict are a natural part of life. When we greet them with courage, and listen to what they tell us, we grow in wisdom, resilience and creativity.</p>
  <p class="front-about">Norah Castell is a coach, educator and mediator. She works with people who want to harvest the fruits of challenge and conflict so they live life differently.</p>
</section>

<section class="flyer flyer-back">
  <svg class="shapes" width="880" height="440" viewBox="0 0 880 440">
    <defs>
      <linearGradient id="backField" x1="0" y1="0" x2="1" y2="1">
        <stop offset="0" stop-color="var(--teal)"/>
        <stop offset=".5" stop-color="var(--green-deep)"/>
        <stop offset="1" stop-color="var(--green-soft)"/>
      </linearGradient>
      <radialGradient id="spiral" cx=".5" cy=".5" r=".5">
        <stop offset="0" stop-color="#6b8c55" stop-opacity="0"/>
        <stop offset=".5" stop-color="#8a5a3a" stop-opacity=".55"/>
        <stop offset=".8" stop-color="#7a4a2c"/>
        <stop offset="1" stop-color="#7a4a2c" stop-opacity="0"/>
      </radialGradient>
    </defs>
    <rect width="880" height="440" fill="url(#backField)"/>
    <circle cx="730" cy="200" r="230" fill="var(--white)" opacity=".06"/>
    <circle cx="725" cy="200" r="135" fill="url(#spiral)" role="img" aria-label="Hand-painted brown brush spiral"/>
  </svg>
  <h2 class="back-name">Norah Castell</h2>
  <p class="back-credentials">PhD, MCR, BAppSci, DipHum, AssDipEd</p>
  <div class="back-copy">
    <p>Consult with Norah to address challenges in your life, relationship, group or organisation. Through listening, conversation and creative processes, you will discover what your challenge is asking of you. Norah Castell is a skilled facilitator who works to shift people's responses from reactivity to creativity.</p>
    <p>With many years' experience in coaching and mentorship, mediation and narrative processes, Norah supports you to uncover unique responses to difficult situations.</p>
  </div>
  <ul class="back-services">
    <li><svg viewBox="0 0 14 14"><path d="M1 1 L13 7 L1 13 L4 7 Z" fill="none" stroke="#fff" stroke-width="1.3"/></svg>Articles</li>
    <li><svg viewBox="0 0 14 14"><path d="M1 1 L13 7 L1 13 L4 7 Z" fill="none" stroke="#fff" stroke-width="1.3"/></svg>Speaking</li>
    <li><svg viewBox="0 0 14 14"><path d="M1 1 L13 7 L1 13 L4 7 Z" fill="none" stroke="#fff" stroke-width="1.3"/></svg>Workshops</li>
    <li><svg viewBox="0 0 14 14"><path d="M1 1 L13 7 L1 13 L4 7 Z" fill="none" stroke="#fff" stroke-width="1.3"/></svg>Consultations</li>
  </ul>
  <footer class="back-footer">
    <div class="contact contact-mobile"><svg viewBox="0 0 16 16"><rect x="4" y="1" width="8" height="14" rx="1.5" fill="none" stroke="#fff" stroke-width="1.3"/><line x1="7" y1="12.5" x2="9" y2="12.5" stroke="#fff"/></svg>0400 555 318</div>
    <div class="contact contact-phone"><svg viewBox="0 0 16 16"><path d="M2 6 Q8 1 14 6 L12 8 L10 6.5 L6 6.5 L4 8 Z" fill="#fff"/><rect x="4" y="9" width="8" height="5" rx="1" fill="#fff"/></svg>+61 3 9000 4417</div>
    <div class="contact contact-email"><svg viewBox="0 0 16 16"><rect x="1.5" y="3.5" width="13" height="9" fill="none" stroke="#fff" stroke-width="1.2"/><path d="M1.5 3.5 L8 9 L14.5 3.5" fill="none" stroke="#fff" stroke-width="1.2"/></svg>norah@norahcastell.com</div>
    <div class="contact contact-web"><svg viewBox="0 0 16 16"><circle cx="8" cy="8" r="6.5" fill="none" stroke="#fff" stroke-width="1.2"/><ellipse cx="8" cy="8" rx="3" ry="6.5" fill="none" stroke="#fff" stroke-width="1"/><line x1="1.5" y1="8" x2="14.5" y2="8" stroke="#fff"/></svg>www.norahcastell.com</div>
    <div class="business-number">ABN 12 345 678 90</div>
  </footer>
</section>

</body>
</html>
```